Flyer Designer for a Widow and Door Company - loooking for fresh design

We are looking for a flyer designed to advertise our business - we supply and install windows and doors - we are looking for a fresh looking flyer to distribute to drum up business - more information can be found at our website www.brightpanehouse.co.uk - We want a different approach than we currently have - making it vibrant and fresh - you can see the services on the website but its more the graphical design that we are looking for rather than content as the content from the website can be used for each service etc.

Target Market(s)

the general public

Colors

Designer to choose colors to be used in the design.

Requirements
Must have
• vibrant design and images

```html
<!DOCTYPE html>
<html lang="en">
<head>
<meta charset="utf-8">
<title>Bright Pane House – Flyer</title>
<link href="https://fonts.googleapis.com/css2?family=Fresca&family=Lato:wght@400;700&display=swap" rel="stylesheet">
<style>
  :root {
    --navy: #0a2a52;
    --blue: #2e6db4;
    --ink: #1a1a1a;
    --icon-grey: #6f7580;
    --footer: #454545;
    --page-bg: #e9eaec;
    --white: #ffffff;
  }
  * { margin: 0; padding: 0; box-sizing: border-box; }
  html, body { width: 1200px; height: 1200px; overflow: hidden; background: var(--page-bg); }
  .flyer {
    position: absolute; left: 0; top: 0;
    width: 904px; height: 1270px;
    background: var(--white);
    transform-origin: 0 0;
    transform: translate(187px, 20px) scale(0.9134);
    font-family: "Lato", sans-serif;
    color: var(--ink);
    overflow: hidden;
  }
  .hero-photo {
    position: absolute; left: 0; top: 0; width: 904px; height: 472px;
    background: linear-gradient(180deg, #6f86c2 0%, #a9aed3 35%, #b89d86 62%, #7d6a55 82%, #4b6a33 100%);
  }
  .banner { position: absolute; left: 0; top: 0; width: 904px; height: 760px; }
  .brand-badge {
    position: absolute; left: 39px; top: 347px; width: 236px; height: 236px;
    border-radius: 50%; background: var(--white);
    box-shadow: 0 0 0 10px var(--navy);
    display: flex; align-items: center; justify-content: center; gap: 10px;
  }
  .brand-badge .mark { width: 30px; height: 30px; background: var(--blue); }
  .brand-badge .name { font-family: "Lato", sans-serif; font-weight: 700; font-size: 21px; line-height: 1.15; color: var(--navy); width: 130px; }
  .headline {
    position: absolute; left: 280px; top: 508px; width: 610px;
    font-family: "Fresca", sans-serif; color: var(--white);
    font-size: 48px; line-height: 50px; text-align: center;
  }
  .services-title {
    position: absolute; left: 484px; top: 675px; width: 240px; height: 47px;
    background: var(--blue); border-radius: 24px;
    font-family: "Fresca", sans-serif; color: var(--white);
    font-size: 40px; line-height: 47px; text-align: center;
  }
  .service { position: absolute; left: 339px; width: 530px; }
  .service .icon { position: absolute; left: 0; width: 64px; height: 64px; }
  .service p { position: absolute; left: 74px; top: 0; width: 452px; font-size: 14.5px; line-height: 17.8px; }
  .project-photo {
    position: absolute; left: 34px; width: 253px;
    border: 5px solid var(--navy);
  }
  .project-photo.doors-a { top: 753px; height: 179px; background: linear-gradient(90deg, #8a7b6e 0%, #b9b9b5 25%, #6b5a4e 50%, #3e3f44 75%, #8a6a58 100%); }
  .project-photo.doors-b { top: 957px; height: 166px; background: linear-gradient(90deg, #8c7c66 0%, #5a2a2a 25%, #8f8270 50%, #9bbab0 75%, #7c6c58 100%); }
  .about { position: absolute; left: 20px; top: 1143px; width: 300px; font-size: 15px; line-height: 17.8px; }
  .footer {
    position: absolute; left: 0; top: 1207px; width: 904px; height: 63px;
    background: var(--footer); color: var(--white);
    font-size: 20px; line-height: 50px; text-align: center; padding-right: 40px;
  }
</style>
</head>
<body>
<div class="flyer">
  <div class="hero-photo" role="img" aria-label="Photo of a large two-storey family house with lit windows and a double garage at dusk"></div>

  <svg class="banner" viewBox="0 0 904 760" aria-hidden="true">
    <polygon points="0,472 904,472 904,672 0,605" fill="var(--navy)"/>
    <polygon points="14,607 275,626 275,640 14,650" fill="#000"/>
    <polygon points="14,650 275,624 275,672 224,672" fill="var(--blue)"/>
    <polygon points="224,672 275,672 224,742" fill="var(--navy)"/>
  </svg>

  <div class="brand-badge">
    <span class="mark"></span>
    <span class="name">Bright Pane House</span>
  </div>

  <h1 class="headline">Transfer the look of your home<br>with a NEW FRONT DOOR</h1>

  <div class="services-title">Our Services</div>

  <div class="service" style="top:738px">
    <svg class="icon" style="top:12px" viewBox="0 0 64 64" aria-hidden="true">
      <circle cx="32" cy="32" r="32" fill="var(--icon-grey)"/>
      <rect x="19" y="14" width="26" height="36" fill="var(--navy)"/>
      <rect x="22" y="17" width="20" height="30" fill="var(--white)"/>
      <path d="M22 27h20M22 37h20M32 17v30" stroke="var(--navy)" stroke-width="3"/>
    </svg>
    <p>Our windows are individually designed to suit your home. Bespoke to your individual requirements.Our windows offer an excepional level of energy efficency with market leading locking systems. With an extensive choice of styles, colours and finishes, do not hesitate in contacting us today to discuss your requirements.</p>
  </div>

  <div class="service" style="top:872px">
    <svg class="icon" style="top:13px" viewBox="0 0 64 64" aria-hidden="true">
      <circle cx="32" cy="32" r="32" fill="var(--icon-grey)"/>
      <rect x="20" y="13" width="24" height="38" fill="var(--navy)"/>
      <polygon points="23,16 37,19 37,52 23,49" fill="#1e56c8"/>
      <rect x="38" y="16" width="3" height="32" fill="var(--white)"/>
      <circle cx="34" cy="34" r="1.6" fill="var(--white)"/>
    </svg>
    <p>A new door from Bright Pane House can transform the look of your home, offer increased thermal efficiency and dramatically improve security for your peace of mind. With literally hundreds of different designs, colours and finishes to choose from, contact us today for a free, no obligation quotation.</p>
  </div>

  <div class="service" style="top:998px">
    <svg class="icon" style="top:2px" viewBox="0 0 64 64" aria-hidden="true">
      <circle cx="32" cy="32" r="32" fill="var(--icon-grey)"/>
      <path d="M18 46 L40 24" stroke="var(--navy)" stroke-width="6" stroke-linecap="round"/>
      <circle cx="43" cy="21" r="7" fill="none" stroke="var(--navy)" stroke-width="4"/>
      <path d="M22 18 L46 44" stroke="#1e56c8" stroke-width="6" stroke-linecap="round"/>
      <path d="M16 16 l6 -2 l2 6 z" fill="var(--navy)"/>
    </svg>
    <p>At Bright Pane House we offer a full repair and replacement service on glass units, windows and doors. No job is too small. Please contact one of our helpful advisors for a non obligatory quotation or to learn more please click the link below.</p>
  </div>

  <div class="service" style="top:1105px">
    <svg class="icon" style="top:10px" viewBox="0 0 64 64" aria-hidden="true">
      <circle cx="32" cy="32" r="32" fill="var(--icon-grey)"/>
      <path d="M16 28 L32 15 L48 28 V44 H26 L18 52 V44 H16 Z" fill="#1e56c8"/>
    </svg>
    <p>We work closely with Landlords &amp; Letting Agents to offer a full repair or replacement service on glass units, windows and doors as well as adjustments and replacement or repair of hinges, handles locks and cylinders. We also offer property surveys &nbsp;and recommendations on the condition of the current windows and doors.</p>
  </div>

  <div class="project-photo doors-a" role="img" aria-label="Before and after photo of a glazed double door replaced by a dark grey composite door with side panels"></div>
  <div class="project-photo doors-b" role="img" aria-label="Before and after photo of a red front door replaced by a pale green door in a stone wall"></div>

  <p class="about">Bright Pane House are Suppliers and installers of quality windows and doors across Northamptonshire and surrounding villages.</p>

  <div class="footer">www.brightpanehouse.co.uk</div>
</div>
</body>
</html>
```